Pest Control Company needs business card!

Hi there, we need a business card designed for our new Pest Control Company. Ideally this card will be simple, yet feel elegant and high end. We want to use the colours Orange, Black and White. Please see our attached logo for the exact colours.

Business card details:

Phone - 0461 275 804
Name - Gavin Holloway
Email - Info@steadfastverminguard.com.au

We would also like to include the following list with dot points:

SERVICES / INSPECTIONS

Termites, Wood Borers, Ants, Cockroaches, Spiders, Fleas, Mice, Rats, Bed Bugs, & More!

```html
<!DOCTYPE html>
<html lang="en">
<head>
<meta charset="utf-8">
<title>Steadfast Vermin Guard – Business Card</title>
<link rel="stylesheet" href="https://fonts.googleapis.com/css2?family=Fredoka:wght@500;600;700&display=swap">
<style>
  :root {
    --backdrop: #e6e6e6;
    --card-black: #231f20;
    --card-yellow: #fec416;
    --yellow-shade: #eab30f;
    --orange: #f47b20;
    --red: #e02027;
    --ink: #1d1d1f;
  }
  * { box-sizing: border-box; margin: 0; padding: 0; }
  html, body {
    width: 1200px; height: 906px; overflow: hidden;
    background: var(--backdrop);
    font-family: "Fredoka", "Arial Rounded MT Bold", sans-serif;
  }
  .canvas { position: relative; width: 1200px; height: 906px; }

  .card {
    position: absolute;
    width: 600px; height: 343px;
    border-radius: 26px;
    overflow: hidden;
  }

  /* Back side */
  .card--back {
    left: 520px; top: 80px;
    background: var(--card-black);
    color: var(--orange);
    display: flex; flex-direction: column; align-items: center; justify-content: center;
    gap: 42px;
  }
  .brand {
    display: flex; align-items: center; gap: 14px;
    font-weight: 700; text-transform: uppercase; line-height: 1;
  }
  .brand__dot { border-radius: 50%; flex: none; }
  .card--back .brand { font-size: 40px; }
  .card--back .brand__dot { width: 30px; height: 30px; background: var(--orange); }

  .services {
    list-style: none;
    display: flex; flex-wrap: wrap; justify-content: center;
    gap: 6px 16px;
    width: 470px;
    font-weight: 600; font-size: 15px; text-transform: uppercase; letter-spacing: 0.2px;
  }
  .services li { display: flex; align-items: center; gap: 5px; }
  .services li::before {
    content: ""; width: 7px; height: 7px; border-radius: 50%; background: var(--red);
  }

  /* Front side */
  .card--front {
    left: 80px; top: 470px;
    background: var(--card-yellow);
    color: var(--ink);
  }
  .card--front .brand {
    position: absolute; left: 48px; top: 46px;
    font-size: 30px; color: var(--ink);
  }
  .card--front .brand__dot { width: 24px; height: 24px; background: var(--ink); }

  .mascot-area {
    position: absolute; right: 0; top: 0;
    width: 260px; height: 343px;
    background: radial-gradient(ellipse at 55% 60%, var(--yellow-shade) 0%, var(--card-yellow) 70%);
  }

  .contact {
    position: absolute; left: 48px; top: 160px;
  }
  .contact__name {
    font-weight: 700; font-size: 24px; text-transform: uppercase; margin-bottom: 18px;
  }
  .contact__line {
    display: flex; align-items: center; gap: 10px;
    font-weight: 600; font-size: 17px; margin-bottom: 10px;
  }
  .contact__icon { width: 18px; height: 18px; flex: none; }
</style>
</head>
<body>
<div class="canvas">

  <section class="card card--back" aria-label="Card back">
    <div class="brand"><span class="brand__dot"></span>Steadfast Vermin Guard</div>
    <ul class="services">
      <li>Termites</li>
      <li>Wood Borers</li>
      <li>Ants</li>
      <li>Cockroaches</li>
      <li>Spiders</li>
      <li>Fleas</li>
      <li>Mice</li>
      <li>Rats</li>
      <li>Bed Bugs, &amp; More!</li>
    </ul>
  </section>

  <section class="card card--front" aria-label="Card front">
    <div class="mascot-area" role="img" aria-label="Large faint cartoon bug mascot with a red exclamation mark"></div>
    <div class="brand"><span class="brand__dot"></span>Steadfast Vermin Guard</div>
    <div class="contact">
      <p class="contact__name">Gavin Holloway</p>
      <p class="contact__line">
        <svg class="contact__icon" viewBox="0 0 24 24" aria-hidden="true">
          <circle cx="12" cy="12" r="12" fill="#e02027"/>
          <path d="M8.2 6.5l2 .3 1 2.6-1.3 1.1a7 7 0 0 0 3.6 3.6l1.1-1.3 2.6 1 .3 2a1.6 1.6 0 0 1-1.7 1.5A10 10 0 0 1 6.7 8.2a1.6 1.6 0 0 1 1.5-1.7z" fill="#fec416"/>
        </svg>
        0461 275 804
      </p>
      <p class="contact__line">
        <svg class="contact__icon" viewBox="0 0 24 24" aria-hidden="true">
          <rect x="1" y="5" width="22" height="15" rx="1.5" fill="#e02027"/>
          <path d="M2 6.5l10 7 10-7" fill="none" stroke="#fec416" stroke-width="1.8"/>
        </svg>
        Info@steadfastverminguard.com.au
      </p>
    </div>
  </section>

</div>
</body>
</html>
```